Design a logo and Business Cards for Corbel Ridge Banquet and Convention Centre

Hi there
I need a logo and business card done . It is for Corbel Ridge Manor Banquet & Convention Centre. Please look at the picture in the attached file, the logo needs to have a very classy look and a WOW factor, using the contrast between the Dark Grey, the light green and Gold. It has to be an elegant card. if you can do a logo for Corbel Ridge Manor Banquet & Convention Centre. That would help to. the contest is for 20.00 and we need this done asap!
https://www.kinlinkpages.com/pages/Corbel-Ridge-Manor-Banquet-Hall/917362048153609?bookmark_t=page
Delia Ponzanelli
Director of Catering & Events
289-555-0163
delia@corbelridgemanor.com
the image is a reference for a color guide. The card should have rounded corners. Artwork needs to be in .ai min 300 dpi
the image It is green , gold and charcoal grey. So please use these.
Thanks
Gus

```html
<!DOCTYPE html>
<html lang="en">
<head>
<meta charset="utf-8">
<title>Corbel Ridge Manor Banquet &amp; Convention Centre – Business Card</title>
<link href="https://fonts.googleapis.com/css2?family=Cinzel:wght@500;600&family=Michroma&display=swap" rel="stylesheet">
<style>
  :root {
    --backdrop: #e4e2dd;
    --card-white: #ffffff;
    --charcoal: #2b2b2c;
    --gold: #c9a227;
    --gold-light: #f1d77a;
    --gold-deep: #9c7612;
    --sage: #a9c48a;
    --ink: #3a3a3a;
    --ink-soft: #6b6b6b;
    --shadow: rgba(0, 0, 0, 0.18);
  }
  * { box-sizing: border-box; margin: 0; padding: 0; }
  html, body {
    width: 1200px;
    height: 897px;
    overflow: hidden;
    background: var(--backdrop);
  }
  .canvas {
    position: relative;
    width: 1200px;
    height: 897px;
  }
  .card {
    position: absolute;
    top: 290px;
    width: 530px;
    height: 303px;
    border-radius: 26px;
    box-shadow: 0 10px 28px var(--shadow);
    overflow: hidden;
  }

  /* Front */
  .card-front {
    left: 50px;
    background: var(--card-white);
  }
  .corner-tab {
    position: absolute;
    left: 0;
    width: 16px;
    height: 78px;
    background: linear-gradient(90deg, var(--gold-deep), var(--gold-light) 45%, var(--gold) 70%, var(--gold-deep));
  }
  .corner-tab.top { top: 0; }
  .corner-tab.bottom { bottom: 0; }

  .brand {
    position: absolute;
    left: 34px;
    top: 70px;
    width: 230px;
    text-align: center;
  }
  .brand-dot {
    display: block;
    width: 46px;
    height: 46px;
    margin: 0 auto 16px;
    border-radius: 50%;
    background: var(--gold);
  }
  .brand-name {
    font-family: "Cinzel", serif;
    font-weight: 600;
    font-size: 13px;
    line-height: 1.25;
    letter-spacing: 0.2px;
    white-space: nowrap;
    color: var(--gold);
  }
  .brand-sub {
    margin-top: 3px;
    font-family: "Cinzel", serif;
    font-weight: 600;
    font-size: 9.5px;
    letter-spacing: 0.6px;
    color: var(--gold);
  }

  .divider {
    position: absolute;
    left: 276px;
    top: 44px;
    width: 1.5px;
    height: 215px;
    background: var(--sage);
  }

  .contact-list {
    position: absolute;
    left: 296px;
    top: 46px;
    list-style: none;
    font-family: "Michroma", sans-serif;
    font-size: 10.5px;
    color: var(--ink);
  }
  .contact-list li {
    display: flex;
    align-items: center;
    height: 20px;
    white-space: nowrap;
  }
  .contact-icon {
    width: 11px;
    height: 11px;
    margin-right: 9px;
    flex: none;
  }

  .person {
    position: absolute;
    left: 296px;
    top: 168px;
    font-family: "Michroma", sans-serif;
  }
  .person-name {
    font-size: 12.5px;
    letter-spacing: 1px;
    color: var(--gold);
    text-transform: uppercase;
  }
  .person-title {
    margin-top: 5px;
    font-size: 10px;
    color: var(--ink-soft);
  }
  .person-address {
    margin-top: 16px;
    font-size: 10px;
    line-height: 1.7;
    color: var(--ink);
  }

  /* Back */
  .card-back {
    left: 620px;
    background: var(--charcoal);
  }
  .back-brand {
    position: absolute;
    left: 44px;
    top: 54px;
  }
  .back-name {
    font-family: "Cinzel", serif;
    font-weight: 600;
    font-size: 18px;
    letter-spacing: 0.6px;
    color: var(--gold);
  }
  .back-sub {
    margin-top: 4px;
    font-family: "Cinzel", serif;
    font-weight: 500;
    font-size: 11px;
    letter-spacing: 1px;
    color: var(--sage);
  }
  .back-dot {
    position: absolute;
    right: 70px;
    bottom: 58px;
    width: 110px;
    height: 110px;
    border-radius: 50%;
    background: linear-gradient(135deg, var(--gold-light), var(--gold) 55%, var(--gold-deep));
  }
</style>
</head>
<body>
<main class="canvas">

  <section class="card card-front" aria-label="Business card front">
    <span class="corner-tab top"></span>
    <span class="corner-tab bottom"></span>

    <div class="brand">
      <span class="brand-dot"></span>
      <p class="brand-name">Corbel Ridge Manor Banquet</p>
      <p class="brand-sub">&amp; Convention Centre</p>
    </div>

    <span class="divider"></span>

    <ul class="contact-list">
      <li>
        <svg class="contact-icon" viewBox="0 0 12 12"><circle cx="6" cy="6" r="6" fill="#c9a227"/><path d="M4 3.2l1.2 1.4-.6.7a4 4 0 0 0 2.1 2.1l.7-.6 1.4 1.2-.6.9C6 8.6 3.4 6 3.1 3.8z" fill="#fff"/></svg>
        289-555-0148
      </li>
      <li>
        <svg class="contact-icon" viewBox="0 0 12 12"><circle cx="6" cy="6" r="6" fill="#c9a227"/><path d="M4 3.2l1.2 1.4-.6.7a4 4 0 0 0 2.1 2.1l.7-.6 1.4 1.2-.6.9C6 8.6 3.4 6 3.1 3.8z" fill="#fff"/></svg>
        289-555-0172
      </li>
      <li>
        <svg class="contact-icon" viewBox="0 0 12 12"><circle cx="6" cy="6" r="6" fill="#c9a227"/><rect x="3.2" y="4.3" width="5.6" height="3.4" fill="#fff"/></svg>
        289-555-0190
      </li>
      <li>
        <svg class="contact-icon" viewBox="0 0 12 12"><circle cx="6" cy="6" r="6" fill="#c9a227"/><path d="M3 4h6v4H3z M3 4l3 2.2L9 4" fill="none" stroke="#fff" stroke-width=".9"/></svg>
        name@corbelridgemanor.com
      </li>
      <li>
        <svg class="contact-icon" viewBox="0 0 12 12"><circle cx="6" cy="6" r="6" fill="#c9a227"/><circle cx="6" cy="6" r="2.8" fill="none" stroke="#fff" stroke-width=".9"/><path d="M3.2 6h5.6" stroke="#fff" stroke-width=".9"/></svg>
        www.corbelridgemanor.com
      </li>
    </ul>

    <div class="person">
      <p class="person-name">Marcus Hale</p>
      <p class="person-title">Owner / C.E.O</p>
      <p class="person-address">Suite # 214, Elm Bldg,<br>ON L7G 5K2</p>
    </div>
  </section>

  <section class="card card-back" aria-label="Business card back">
    <div class="back-brand">
      <p class="back-name">Corbel Ridge Manor Banquet</p>
      <p class="back-sub">&amp; Convention Centre</p>
    </div>
    <span class="back-dot"></span>
  </section>

</main>
</body>
</html>
```